Valentine's Day Flyer

We require an A5 size flyer to promote our February parking offer & Giveaway.

Offer:
Book your parking online & Save!
$5 Night/Weekend Parking
$10 Early Bird Parking

Giveaway: Win a $5,000 Diamond Ring!
Every time you book your parking online using Trundle-Nook you get a chance to win!

The final design should contain:
- Valentine's Theme
- Emphasise 'Book your parking online & Save!'

Designers: please visit www.halvorbaypark.com.au for more info on Halvor Bay Parking & Trundle-Nook

Target Market(s)

18-50 year old drivers

Industry/Entity Type

Parking

```html
<!DOCTYPE html>
<html lang="en">
<head>
<meta charset="utf-8">
<title>Halvor Bay Parking – Valentine's Flyer</title>
<link rel="stylesheet" href="https://fonts.googleapis.com/css2?family=Roboto+Condensed:wght@700&family=Roboto:wght@400;500;700&display=swap">
<style>
  :root {
    --sky: #acdce2;
    --ocean: #0a87be;
    --navy: #1b4a8c;
    --marigold: #e9a944;
    --white: #ffffff;
    --page: #ffffff;
  }
  * { margin: 0; padding: 0; box-sizing: border-box; }
  html, body { width: 1200px; height: 1000px; overflow: hidden; background: var(--page); }
  .canvas { position: relative; width: 1200px; height: 1000px; }
  .flyer {
    position: absolute; left: 262px; top: 20px; width: 676px; height: 960px;
    overflow: hidden; font-family: "Roboto", Arial, sans-serif;
  }
  .flyer-shapes { position: absolute; inset: 0; }
  .headline {
    position: absolute; left: 0; right: 0; top: 38px; text-align: center;
    font-family: "Roboto Condensed", "Arial Narrow", sans-serif; font-weight: 700;
    color: var(--white); font-size: 56px; line-height: 64px; letter-spacing: 0.5px;
  }
  .headline .highlight {
    display: inline-block; color: var(--marigold);
    border: 2px solid var(--white); padding: 0 8px; line-height: 58px; margin-right: 4px;
  }
  .offer { position: absolute; color: var(--white); font-weight: 700; font-size: 19px; white-space: nowrap; }
  .offer .price { color: var(--navy); font-size: 34px; margin-right: 6px; }
  .offer-night { left: 205px; top: 322px; }
  .offer-early { left: 223px; top: 378px; }
  .giveaway {
    position: absolute; left: 0; right: 0; top: 622px; text-align: center;
    font-family: "Roboto Condensed", "Arial Narrow", sans-serif; font-weight: 700;
    color: var(--navy); font-size: 34px;
  }
  .giveaway-detail {
    position: absolute; left: 0; right: 0; top: 726px; text-align: center;
    color: var(--ocean); font-weight: 500; font-size: 23px; line-height: 29px;
  }
  .brand { position: absolute; left: 45px; top: 826px; display: flex; align-items: center; gap: 12px; }
  .brand-square { width: 58px; height: 58px; background: var(--navy); }
  .brand-name { color: var(--navy); font-weight: 700; font-size: 21px; line-height: 25px; }
  .contact { position: absolute; left: 330px; top: 842px; font-size: 20px; line-height: 27px; }
  .contact .tagline { color: var(--navy); }
  .contact .web { color: var(--white); font-weight: 700; }
</style>
</head>
<body>
<div class="canvas">
  <section class="flyer">
    <svg class="flyer-shapes" width="676" height="960" viewBox="0 0 676 960">
      <rect class="sky-band" width="676" height="960" fill="var(--sky)"/>
      <rect class="marigold-base" y="450" width="676" height="510" fill="var(--marigold)"/>
      <path class="heart-pattern-band" role="img" aria-label="Blue band with a repeating pattern of outlined hearts"
            d="M0,260 Q338,90 676,260 L676,520 Q338,654 0,520 Z" fill="var(--ocean)"/>
      <path class="offer-heart" d="M346,572 L188,402 C126,334 150,218 252,218 C302,218 336,256 346,296 C356,256 390,218 440,218 C542,218 566,334 504,402 Z"
            fill="var(--marigold)" stroke="var(--white)" stroke-width="26" stroke-linejoin="round"/>
      <path class="detail-lens" d="M30,749 Q338,610 646,749 Q338,888 30,749 Z" fill="var(--white)"/>
    </svg>

    <h1 class="headline">BOOK YOUR PARKING<br><span class="highlight">ONLINE</span> &amp; SAVE!</h1>

    <p class="offer offer-night"><span class="price">$5</span>Night/Weekend Parking</p>
    <p class="offer offer-early"><span class="price">$10</span>Early Bird Parking</p>

    <h2 class="giveaway">Giveaway: Win a $5,000 Diamond Ring!</h2>
    <p class="giveaway-detail">Every time you book your parking online using<br>Trundle-Nook you get a chance to win!</p>

    <div class="brand">
      <div class="brand-square"></div>
      <div class="brand-name">Halvor Bay<br>Parking</div>
    </div>
    <div class="contact">
      <p class="tagline">Plan before you Park</p>
      <p class="web">www.halvorbaypark.com.au</p>
    </div>
  </section>
</div>
</body>
</html>
```